New business card for UK roofing company

We are Penwick Roofing and we need a business card design for our staff.

We offer the following services:

- New roofs
- General roof repairs
- Drone surveys
- Single ply roofing
- Steel cladding
- Asbestos removal
- Electronic leak detection

I have attached our logo. I have also attached example branding printed to our vans. The business card should fit in with the style of our branding.

The business card should have the following information;

Address:
Unit 17c Marlow Dene Farm
Marlow Dene Lane
Fenbury
RX4 9QD

Telephone: 020 7946 0312
24 Hour: 0800 471 9062

Email: tom@penwickroofing.com
Mobile: 07700900418
Name: Tom Harley
Website: www.penwickroofing.com

The business card will be printed in Spot UV, see here: https://www.printvane.com/business-cards/spot-uv/

If you need anymore info, please let me know,

```html
<!DOCTYPE html>
<html lang="en">
<head>
<meta charset="utf-8">
<title>Penwick Roofing – Business Card</title>
<link href="https://fonts.googleapis.com/css2?family=Poppins:wght@400;600;700&display=swap" rel="stylesheet">
<style>
  :root {
    --navy: #0d4d80;
    --navy-deep: #0b3f6e;
    --sky: #10b0e0;
    --white: #ffffff;
    --ink: #1c1c1c;
    --stage: #2a2b2d;
  }
  * { margin: 0; padding: 0; box-sizing: border-box; }
  html, body { width: 1200px; height: 1015px; overflow: hidden; }
  body {
    background: var(--stage);
    font-family: "Poppins", sans-serif;
    position: relative;
  }
  .card {
    position: absolute;
    left: 290px;
    width: 620px;
    height: 360px;
    overflow: hidden;
  }
  /* Back of card */
  .card--back { top: 100px; background: var(--navy); color: var(--white); text-align: center; }
  .brand {
    display: flex; align-items: center; justify-content: center; gap: 14px;
    margin-top: 92px;
  }
  .brand__dot { width: 48px; height: 48px; border-radius: 50%; background: var(--sky); }
  .brand__name { font-weight: 700; font-size: 44px; letter-spacing: -1px; color: var(--white); line-height: 1; }
  .services { margin-top: 42px; font-size: 15px; line-height: 1.35; }
  .services__title { color: var(--sky); font-weight: 700; text-transform: uppercase; font-size: 14px; letter-spacing: 0.3px; }
  .services .sep { color: var(--sky); padding: 0 4px; }

  /* Front of card */
  .card--front { top: 555px; background: var(--white); color: var(--ink); }
  .holder { position: absolute; left: 34px; top: 52px; display: flex; align-items: center; gap: 12px; }
  .holder__bars { display: flex; gap: 4px; }
  .holder__bars span { width: 8px; height: 30px; background: var(--navy-deep); transform: skewX(-18deg); }
  .holder__bars span + span { background: var(--sky); }
  .holder__name { font-size: 28px; font-weight: 700; color: var(--navy-deep); }
  .holder__name em { font-style: normal; color: var(--sky); }

  .contact { position: absolute; left: 62px; top: 112px; list-style: none; font-size: 15px; }
  .contact li { display: flex; align-items: center; gap: 8px; height: 22px; }
  .contact li.gap { margin-top: 12px; }
  .contact .hl { color: var(--navy-deep); font-weight: 600; }
  .icon { width: 18px; height: 18px; flex: none; }
  .address { position: absolute; left: 62px; top: 262px; display: flex; gap: 8px; font-size: 15px; line-height: 1.3; }
  .address .icon { margin-top: 1px; }

  .emblem {
    position: absolute; right: 34px; top: 54px;
    width: 220px; height: 220px; border-radius: 50%;
    background: var(--sky); border: 4px solid var(--white);
    box-shadow: 0 0 0 3px var(--navy-deep);
  }
</style>
</head>
<body>

<section class="card card--back">
  <div class="brand">
    <span class="brand__dot"></span>
    <span class="brand__name">penwickroofing</span>
  </div>
  <div class="services">
    <p class="services__title">We offer the following services:</p>
    <p>New roofs <span class="sep">|</span> General roof repairs <span class="sep">|</span> Drone surveys</p>
    <p>Single ply roofing <span class="sep">|</span> Steel cladding</p>
    <p>Asbestos removal <span class="sep">|</span> Electronic leak detection</p>
  </div>
</section>

<section class="card card--front">
  <div class="holder">
    <div class="holder__bars"><span></span><span></span></div>
    <h1 class="holder__name">Tom <em>Harley</em></h1>
  </div>

  <ul class="contact">
    <li>
      <svg class="icon" viewBox="0 0 18 18"><circle cx="9" cy="9" r="9" fill="var(--sky)"/><rect x="6" y="4" width="6" height="10" rx="1" fill="none" stroke="#fff" stroke-width="1.3"/></svg>
      07700900418
    </li>
    <li>
      <svg class="icon" viewBox="0 0 18 18"><circle cx="9" cy="9" r="9" fill="var(--sky)"/><rect x="4.5" y="5.5" width="9" height="7" fill="none" stroke="#fff" stroke-width="1.3"/><path d="M4.5 5.5 9 9.5 13.5 5.5" fill="none" stroke="#fff" stroke-width="1.3"/></svg>
      tom@penwickroofing.com
    </li>
    <li>
      <svg class="icon" viewBox="0 0 18 18"><circle cx="9" cy="9" r="9" fill="var(--sky)"/><circle cx="9" cy="9" r="4.5" fill="none" stroke="#fff" stroke-width="1.2"/><path d="M4.5 9h9M9 4.5c-2 2.5-2 6.5 0 9M9 4.5c2 2.5 2 6.5 0 9" fill="none" stroke="#fff" stroke-width="1"/></svg>
      www.penwickroofing.com
    </li>
    <li class="gap">
      <svg class="icon" viewBox="0 0 18 18"><circle cx="9" cy="9" r="9" fill="var(--sky)"/><path d="M6 4.5l2 2-1.2 1.4a6 6 0 0 0 3.3 3.3l1.4-1.2 2 2-1.5 1.5C8.5 13.5 4.5 9.5 4.5 6z" fill="#fff"/></svg>
      020 7946 0312
    </li>
    <li>
      <svg class="icon" viewBox="0 0 18 18"><circle cx="9" cy="9" r="9" fill="var(--sky)"/><path d="M6 4.5l2 2-1.2 1.4a6 6 0 0 0 3.3 3.3l1.4-1.2 2 2-1.5 1.5C8.5 13.5 4.5 9.5 4.5 6z" fill="#fff"/></svg>
      0800 471 9062&nbsp;<span class="hl">(24 Hour)</span>
    </li>
  </ul>

  <div class="address">
    <svg class="icon" viewBox="0 0 18 18"><circle cx="9" cy="9" r="9" fill="var(--sky)"/><path d="M9 14s-3.5-3.8-3.5-6.2a3.5 3.5 0 0 1 7 0C12.5 10.2 9 14 9 14z" fill="#fff"/><circle cx="9" cy="7.8" r="1.3" fill="var(--sky)"/></svg>
    <address style="font-style:normal">
      Unit 17c Marlow Dene Farm<br>
      Marlow Dene Lane<br>
      Fenbury, RX4 9QD
    </address>
  </div>

  <div class="emblem" aria-hidden="true"></div>
</section>

</body>
</html>
```